Business Card Design needed for logo design project

This project is linked to http://jobs.quillmarket.com/job.aspx?id=472913
Harbor Ledger Dynamics.

Our company needs a Business Card Design. Please refer to our original project in the link above.

We would like the size to be a typical rectangle, no rounded edges or atypical sizes that will be costly to print. Thanks!

Target Market(s)

Small business owners in the U.S.

Industry/Entity Type

Business

```html
<!DOCTYPE html>
<html lang="en">
<head>
<meta charset="utf-8">
<title>Harbor Ledger Dynamics – Business Card</title>
<link href="https://fonts.googleapis.com/css2?family=Montserrat:wght@400;500;600&family=Arimo:wght@400&display=swap" rel="stylesheet">
<style>
  :root {
    --backdrop: #ebebeb;
    --brand-blue: #2457ad;
    --brand-blue-deep: #1d4c9e;
    --brand-blue-light: #3b86d1;
    --card-white: #f2f2f2;
    --ink-grey: #444444;
    --white: #ffffff;
  }
  * { margin: 0; padding: 0; box-sizing: border-box; }
  html, body {
    width: 1200px; height: 675px; overflow: hidden;
    background: var(--backdrop);
  }
  .canvas {
    position: relative; width: 1200px; height: 675px;
    display: flex; align-items: center; justify-content: center; gap: 60px;
  }
  .card {
    position: relative; width: 520px; height: 297px; overflow: hidden;
    box-shadow: 0 6px 18px rgba(0,0,0,0.18);
  }
  /* Front */
  .card-front {
    background: radial-gradient(circle at 40% 30%, var(--brand-blue-light) 0%, var(--brand-blue) 45%, var(--brand-blue-deep) 100%);
  }
  .front-arc { position: absolute; inset: 0; }
  .front-brand {
    position: absolute; left: 0; right: 0; top: 50%; transform: translateY(-50%);
    display: flex; align-items: center; justify-content: center; gap: 14px;
  }
  .brand-dot { width: 18px; height: 18px; border-radius: 50%; background: var(--white); flex: none; }
  .brand-name {
    font-family: "Montserrat", sans-serif; font-weight: 400;
    font-size: 24px; line-height: 1.1; letter-spacing: 0.5px;
    text-transform: uppercase; color: var(--white);
  }
  /* Back */
  .card-back { background: var(--card-white); }
  .back-waves { position: absolute; inset: 0; }
  .back-brand {
    position: absolute; left: 38px; top: 78px;
    display: flex; align-items: center; gap: 10px;
  }
  .back-brand .brand-dot { width: 12px; height: 12px; background: var(--brand-blue); }
  .back-brand .brand-name { font-size: 17px; color: var(--brand-blue); }
  .employee {
    position: absolute; left: 38px; top: 222px;
    font-family: "Montserrat", sans-serif;
  }
  .employee-name { font-size: 12px; font-weight: 600; color: var(--brand-blue); letter-spacing: 0.4px; }
  .employee-title { font-size: 11px; color: var(--ink-grey); margin-top: 2px; }
  .contact {
    position: absolute; right: 20px; top: 112px; text-align: right;
    font-family: "Arimo", sans-serif; font-size: 10.5px; line-height: 1.4;
    color: var(--white); list-style: none;
  }
  .contact li { display: flex; justify-content: flex-end; align-items: center; gap: 5px; }
  .contact .address { margin-bottom: 9px; display: block; }
  .contact-icon { width: 9px; height: 9px; flex: none; }
</style>
</head>
<body>
<main class="canvas">
  <section class="card card-front" aria-label="Business card front">
    <svg class="front-arc" viewBox="0 0 520 297" aria-hidden="true">
      <path d="M60,297 C140,200 300,130 520,110" fill="none" stroke="rgba(255,255,255,0.18)" stroke-width="6"/>
    </svg>
    <div class="front-brand">
      <span class="brand-dot"></span>
      <span class="brand-name">Harbor Ledger<br>Dynamics</span>
    </div>
  </section>

  <section class="card card-back" aria-label="Business card back">
    <svg class="back-waves" viewBox="0 0 520 297" aria-hidden="true">
      <path d="M520,30 C400,30 340,90 315,170 C295,235 245,282 160,297 L520,297 Z" fill="var(--brand-blue)"/>
      <path d="M520,50 C412,50 356,105 333,178 C313,243 262,285 195,297" fill="none" stroke="var(--card-white)" stroke-width="5"/>
      <path d="M105,297 C190,282 262,242 294,168" fill="none" stroke="var(--ink-grey)" stroke-width="10" stroke-linecap="round"/>
    </svg>
    <div class="back-brand">
      <span class="brand-dot"></span>
      <span class="brand-name">Harbor Ledger<br>Dynamics</span>
    </div>
    <div class="employee">
      <p class="employee-name">EMPLOYEE NAME</p>
      <p class="employee-title">Title</p>
    </div>
    <ul class="contact">
      <li class="address">4120 Alder Crest Rd Suite 200,<br>Oregon USA 97201</li>
      <li>800.555.0142
        <svg class="contact-icon" viewBox="0 0 10 10"><circle cx="5" cy="5" r="5" fill="#fff"/><path d="M3,2.5 L4.2,2.5 L4.6,4 L3.9,4.5 C4.3,5.3 4.7,5.7 5.5,6.1 L6,5.4 L7.5,5.8 L7.5,7 C5,7 3,5 3,2.5Z" fill="var(--brand-blue)"/></svg></li>
      <li>800.555.0187
        <svg class="contact-icon" viewBox="0 0 10 10"><rect x="1" y="2" width="8" height="6" fill="#fff"/></svg></li>
      <li>info@harborledger.com
        <svg class="contact-icon" viewBox="0 0 10 10"><rect x="0.5" y="2" width="9" height="6" fill="#fff"/><path d="M0.5,2 L5,5.5 L9.5,2" fill="none" stroke="var(--brand-blue)" stroke-width="0.8"/></svg></li>
      <li>www.harborledger.com
        <svg class="contact-icon" viewBox="0 0 10 10"><circle cx="5" cy="5" r="4.3" fill="none" stroke="#fff" stroke-width="1"/><path d="M0.7,5 H9.3 M5,0.7 C3,3 3,7 5,9.3 M5,0.7 C7,3 7,7 5,9.3" fill="none" stroke="#fff" stroke-width="0.7"/></svg></li>
    </ul>
  </section>
</main>
</body>
</html>
```